Business Card Design & logo

Residential building renovation and maintenance work.
All carpentry and joinery needs.
Laying solid timber and floating floors.
Kitchen and bathroom makeovers and modifications.
Interior fitouts,
small job specialist. tiling, plastering, painting,

I would like a silver background. With the use of different shades of grey, rustic orange, black and white.
I do not want pictures of hammers, chisels etc. I am looking for a logo to be incorporated into the card.

Industry/Entity Type

Carpentry

Contact Information for Business Card

BTW Renovations and Maintenance
Lionel Pasquet
0471526083
info@btwrefits.com.au
btwrefits.com.au

```html
<!DOCTYPE html>
<html lang="en">
<head>
<meta charset="utf-8">
<title>BTW Renovations &amp; Maintenance – Business Card</title>
<link rel="stylesheet" href="https://fonts.googleapis.com/css2?family=PT+Sans:wght@400;700&family=PT+Sans+Narrow:wght@700&display=swap">
<style>
  :root {
    --navy: #2b2466;
    --orange: #f7941d;
    --grey-text: #8a8a8a;
    --silver-light: #f4f6f8;
    --silver-mid: #c9d0d8;
    --silver-dark: #9aa6b2;
    --white: #ffffff;
    --page: #ffffff;
  }
  * { box-sizing: border-box; margin: 0; padding: 0; }
  html, body {
    width: 1200px; height: 1000px; overflow: hidden;
    background: var(--page);
    font-family: "PT Sans", Arial, sans-serif;
  }
  .canvas { position: relative; width: 1200px; height: 1000px; }

  .card {
    position: absolute;
    width: 560px; height: 340px;
    overflow: hidden;
    box-shadow: 0 6px 18px rgba(0,0,0,0.18);
  }
  .card-front { left: 60px; top: 50px; background: var(--white); }
  .card-back {
    left: 620px; top: 320px;
    background: linear-gradient(160deg, var(--silver-dark) 0%, var(--silver-mid) 35%, var(--silver-light) 70%, var(--white) 100%);
  }
  .card-shapes { position: absolute; inset: 0; }

  .wordmark {
    display: flex; align-items: center; gap: 10px;
    color: var(--navy);
    font-family: "PT Sans Narrow", "PT Sans", sans-serif;
    font-weight: 700;
    line-height: 1.05;
  }
  .wordmark-square { flex: none; background: var(--orange); }

  .card-front .wordmark { position: absolute; left: 140px; top: 44px; font-size: 24px; width: 210px; }
  .card-front .wordmark-square { width: 22px; height: 22px; }

  .contact { position: absolute; left: 44px; bottom: 52px; color: var(--grey-text); font-size: 15px; line-height: 1.35; }
  .contact-name { color: #222; font-weight: 700; font-size: 16px; }
  .contact-role { margin-bottom: 2px; }
  .contact-gap { height: 14px; }
  .contact-line { display: flex; align-items: center; gap: 6px; }
  .contact-line svg { width: 13px; height: 13px; flex: none; }

  .card-back .wordmark { position: absolute; left: 0; right: 0; top: 96px; justify-content: center; font-size: 34px; }
  .card-back .wordmark-square { width: 28px; height: 28px; }
  .card-back .website {
    position: absolute; left: 0; right: 0; top: 232px;
    text-align: center; color: var(--navy); font-size: 22px; letter-spacing: 0.5px;
  }

  .logo-lockup { position: absolute; left: 80px; top: 760px; }
  .logo-lockup .wordmark { font-size: 58px; gap: 18px; }
  .logo-lockup .wordmark-square { width: 48px; height: 48px; }
</style>
</head>
<body>
<main class="canvas">

  <section class="card card-front" aria-label="Business card front">
    <svg class="card-shapes" viewBox="0 0 560 340" aria-hidden="true">
      <polygon points="0,0 120,0 95,20 0,20" fill="var(--orange)"/>
      <path d="M350,0 L560,0 L560,220 C540,120 480,50 350,0 Z" fill="var(--navy)"/>
      <path d="M335,0 C475,50 540,130 560,235" fill="none" stroke="var(--orange)" stroke-width="5"/>
      <polygon points="0,322 560,306 560,340 0,340" fill="var(--navy)"/>
      <line x1="0" y1="316" x2="560" y2="300" stroke="var(--orange)" stroke-width="4"/>
    </svg>
    <div class="wordmark">
      <span class="wordmark-square"></span>
      <span>BTW Renovations &amp; Maintenance</span>
    </div>
    <div class="contact">
      <div class="contact-name">Lionel Pasquet</div>
      <div class="contact-role">Director</div>
      <div class="contact-line">
        <svg viewBox="0 0 12 12"><rect x="3" y="1" width="6" height="10" rx="1" fill="none" stroke="currentColor" stroke-width="1.2"/></svg>
        0471526083
      </div>
      <div class="contact-gap"></div>
      <div>Address will come here</div>
      <div>Address will come here</div>
      <div class="contact-line">
        <svg viewBox="0 0 12 12"><circle cx="6" cy="6" r="5" fill="none" stroke="currentColor" stroke-width="1.1"/><path d="M4,3.5 L5,5 L4.5,6 Q5.5,7.5 6.5,7.6 L7.3,7 L8.6,8" fill="none" stroke="currentColor" stroke-width="1"/></svg>
        (+00) 01234 567 890
      </div>
      <div class="contact-line">
        <svg viewBox="0 0 12 12"><rect x="1" y="2.5" width="10" height="7" fill="none" stroke="currentColor" stroke-width="1.1"/><path d="M1,2.5 L6,6.5 L11,2.5" fill="none" stroke="currentColor" stroke-width="1.1"/></svg>
        info@btwrefits.com.au
      </div>
    </div>
  </section>

  <section class="card card-back" aria-label="Business card back">
    <div class="wordmark">
      <span class="wordmark-square"></span>
      <span>BTW Renovations &amp; Maintenance</span>
    </div>
    <div class="website">www.btwrefits.com.au</div>
  </section>

  <section class="logo-lockup" aria-label="Logo">
    <div class="wordmark">
      <span class="wordmark-square"></span>
      <span>BTW Renovations &amp; Maintenance</span>
    </div>
  </section>

</main>
</body>
</html>
```